LEARN Business Skills so you can Earn a good living

size of the poster is 8”x 10.75" plus 0.25" bleed.
Please leave 1 inch on the bottoum for footer
I want a design a poster that will attract people's attention.
I appreciate a creative ad however the ad should not take away from being able to clearly read the text.
-I also appreciate a simple creative ad that is not too busy.
-you can use graphics, vectors, or pictures of real people.
-however, if you use real people it should be a white male that is wearing a white shirt and look like a professional person.

Target Market(s)

Potential young business people

Industry/Entity Type

education

Requirements
Must have
• easy to read the text
Nice to have
• I would like a "creative" simple ad that is easy to be read
Should not have
• pictures of women

```html
<!DOCTYPE html>
<html lang="en">
<head>
<meta charset="utf-8">
<title>Learn IT to Earn IT – Business Enrichment Course</title>
<link href="https://fonts.googleapis.com/css2?family=Abril+Fatface&family=PT+Sans:wght@400;700&family=Open+Sans:wght@400;600&display=swap" rel="stylesheet">
<style>
  :root{
    --stage:#eceef2;
    --navy:#2a3791;
    --royal:#1b78c3;
    --photo-top:#8e9ec7;
    --photo-mid:#a3b0d2;
    --photo-low:#dfe3ee;
    --figure-top:#7d8fbf;
    --figure-low:#c3cbe2;
    --mist:#e3e6ef;
    --white:#ffffff;
  }
  *{margin:0;padding:0;box-sizing:border-box}
  html,body{width:1200px;height:761px;overflow:hidden;background:var(--stage)}
  .canvas{position:relative;width:1200px;height:761px}
  .poster{position:absolute;left:317px;top:0;width:566px;height:761px;background:var(--white);overflow:hidden}

  .hero{position:absolute;left:0;top:0;width:566px;height:290px;
    background:linear-gradient(180deg,var(--photo-top) 0%,var(--photo-mid) 80%,var(--photo-low) 86%,var(--photo-low) 100%)}
  .hero__instructor{position:absolute;left:402px;top:14px;width:164px;height:276px;
    border-radius:70px 0 0 0;
    background:linear-gradient(180deg,var(--figure-top) 0%,var(--figure-low) 100%)}

  .headline{position:absolute;font-family:"Abril Fatface",serif;line-height:1;white-space:nowrap}
  .headline--learn{left:9px;top:50px;font-size:66px;color:var(--white)}
  .headline--to{left:160px;top:114px;font-size:40px;color:var(--white)}
  .headline--earn{left:8px;top:138px;font-size:71px;color:var(--white)}
  .headline--it-top{left:218px;top:16px;font-size:112px;color:var(--navy);letter-spacing:-2px}
  .headline--it-bottom{left:212px;top:104px;font-size:119px;color:var(--navy);letter-spacing:-2px}

  .course-arrow{position:absolute;left:0;top:290px}
  .course-title{position:absolute;left:0;top:298px;width:328px;text-align:center;
    font-family:"PT Sans",sans-serif;font-weight:700;color:var(--white);font-size:52px;line-height:42px}

  .tagline{position:absolute;left:0;top:448px;width:346px;height:60px;background:var(--royal);
    font-family:"Open Sans",sans-serif;font-weight:600;color:var(--white);font-size:22.8px;line-height:24px;
    text-align:center;padding-top:6px;white-space:nowrap}

  .benefits{position:absolute;left:0;top:508px;width:346px;height:168px;background:var(--mist)}
  .benefits__intro{position:absolute;left:0;top:12px;width:346px;text-align:center;
    font-family:"Open Sans",sans-serif;font-size:16.6px;color:var(--navy)}
  .benefits__box{position:absolute;left:24px;top:64px;width:308px;height:98px;
    border:2.5px solid var(--royal);border-radius:18px}
  .benefits__pill{position:absolute;left:48px;top:38px;width:260px;height:52px;border-radius:26px;
    background:var(--royal);color:var(--white);font-family:"PT Sans",sans-serif;font-weight:700;
    font-size:26.5px;line-height:52px;text-align:center}
  .benefits__line{position:absolute;left:24px;width:308px;text-align:center;
    font-family:"Open Sans",sans-serif;font-size:21px;color:var(--navy)}
  .benefits__line--one{top:98px}
  .benefits__line--two{top:126px}

  .topics{position:absolute;left:346px;top:290px;width:220px;height:386px;background:var(--royal);
    list-style:none;padding:8px 0 0 0}
  .topics li{position:relative;padding-left:17px;font-family:"Open Sans",sans-serif;font-weight:600;
    font-size:12.4px;line-height:17.7px;color:var(--white);white-space:nowrap}
  .topics li::before{content:"";position:absolute;left:6px;top:7px;width:4px;height:4px;border-radius:50%;background:var(--navy)}
</style>
</head>
<body>
<div class="canvas">
  <div class="poster">
    <div class="hero" role="img" aria-label="Blue-tinted classroom chalkboard with a chalk ledge along the bottom">
      <div class="hero__instructor" role="img" aria-label="Photo of a grey-haired male instructor in a white shirt and sweater vest writing on the chalkboard, tinted blue"></div>
    </div>
    <div class="headline headline--learn">Learn</div>
    <div class="headline headline--to">to</div>
    <div class="headline headline--earn">Earn</div>
    <div class="headline headline--it-top">IT</div>
    <div class="headline headline--it-bottom">IT</div>

    <svg class="course-arrow" width="346" height="158" viewBox="0 0 346 158">
      <polygon points="0,0 320,0 346,79 320,158 0,158" fill="var(--navy)"/>
    </svg>
    <div class="course-title">Business<br>Enrichment<br>Course</div>

    <div class="tagline">A proven success of helping<br>people in their livelihoods</div>

    <div class="benefits">
      <p class="benefits__intro">Business skills that will help you:</p>
      <div class="benefits__box"></div>
      <div class="benefits__pill">Get a quality job</div>
      <p class="benefits__line benefits__line--one">- start/grow your business</p>
      <p class="benefits__line benefits__line--two">-Increase your salary</p>
    </div>

    <ul class="topics">
      <li>BUSINESS ADMIISTRATION</li>
      <li>SMALL BUSINESS MANAGEMENT</li>
      <li>FINANCE</li>
      <li>INVESTMENTS</li>
      <li>COMPUTERS</li>
      <li>ACCOUNTING</li>
      <li>SALES &nbsp;MARKETING</li>
      <li>PROJECT MANAGEMENT</li>
      <li>INTERVIEWING SKILLS</li>
      <li>BUSINESS LAW</li>
      <li>NEGOTIATION</li>
      <li>PUBLIC SPEAKING</li>
      <li>IMPORT/EXPORT</li>
      <li>INFORMATION TECHNOLOY</li>
      <li>DISTRIBUTION</li>
      <li>MARKETING</li>
      <li>TALLYBOOKS</li>
      <li>REAL ESTATE</li>
      <li>HEALTH CARE</li>
      <li>MANAGEMENT</li>
      <li>RIVERMART</li>
    </ul>
  </div>
</div>
</body>
</html>
```